Business card design for a dynamic IT consulting company

We need a business card design for a young firm, specialized in the Telecommunications/Consulting industry. The name of the company is Brask and Partners Business Consulting Ltd. (Short name: Brask and Partnes)
Brask = solve read reverse, so we aim to be uncomplicated and solution-oriented. The small pipe in our logo is also related to the word solve. So we need a new business card design, which is simple, eye catching and something non traditional (I would probably prefer a square shaped design rather than a rectangle, but open for suggestions). Attached our logo.

Target Market(s)

Usually our customers are Tier1 Telecoms providers (Q-Linkra, Parnexo, etc) and their executives.

Industry/Entity Type

Business

Contact Information for Business Card

Name: Gergely Halmindo
Email: g.halmindo@braskpartnera.hu
Web: www.braskpartnera.hu
Mobile: +36 30 555 0192
Title: Managing Director

Optional:
Company name: Brask and Partners Ltd.
Address: 1047 Budapest, Ravaszi str. 17/B, Hungary

Font styles to use
Other font styles liked:
• helveticaneue_medium, Prime Regular are used now.

Colors

Designer to choose colors to be used in the design.

Requirements
Must have
• I would like to have a 2 sided design.
Nice to have
• I thought if we make the logo a bit bigger (without the company name), that could go to the back with the company name below. I though, if the pipe in the logo is somehow touchable on the business card, would be nice and unique.

```html
<!DOCTYPE html>
<html lang="en">
<head>
<meta charset="utf-8">
<title>Brask and Partners – Business Card</title>
<link rel="stylesheet" href="https://fonts.googleapis.com/css2?family=Exo+2:wght@500&family=Arimo:wght@400&display=swap">
<style>
  :root {
    --page-bg: #e6e7e9;
    --card-bg: #ffffff;
    --ink: #222326;
    --brand-blue: #0a6fc4;
    --band-start: #0a86cf;
    --band-end: #0a2f9a;
    --accent-magenta: #a0146e;
    --muted: #3a3a3a;
  }
  * { box-sizing: border-box; margin: 0; padding: 0; }
  html, body { width: 1200px; height: 1200px; overflow: hidden; }
  body {
    background: var(--page-bg);
    font-family: "Arimo", Arial, sans-serif;
    color: var(--ink);
    position: relative;
  }
  .card {
    position: absolute;
    left: 180px;
    width: 840px;
    height: 480px;
    background: var(--card-bg);
    box-shadow: 0 6px 18px rgba(0,0,0,0.18);
    overflow: hidden;
  }
  .card--back { top: 80px; }
  .card--front { top: 640px; }

  .wordmark {
    position: absolute;
    display: flex;
    align-items: center;
    gap: 18px;
    font-family: "Exo 2", sans-serif;
    font-weight: 500;
    color: var(--ink);
    white-space: nowrap;
  }
  .wordmark__square {
    width: 26px; height: 26px;
    background: var(--ink);
  }
  .card--back .wordmark {
    left: 50%; top: 160px;
    transform: translateX(-50%);
    font-size: 58px;
  }
  .card--back .company-name {
    position: absolute;
    left: 0; right: 0; top: 280px;
    text-align: center;
    font-family: "Exo 2", sans-serif;
    font-weight: 500;
    font-size: 30px;
    letter-spacing: 1px;
    color: var(--brand-blue);
  }

  .card--front .wordmark {
    right: 60px; top: 40px;
    font-size: 46px;
  }
  .person {
    position: absolute;
    right: 60px; top: 140px;
    text-align: right;
  }
  .person__name {
    font-family: "Exo 2", sans-serif;
    font-weight: 500;
    font-size: 42px;
    color: var(--brand-blue);
    letter-spacing: 1px;
  }
  .person__role {
    margin-top: 6px;
    font-size: 17px;
    color: var(--muted);
    display: flex;
    justify-content: flex-end;
    align-items: center;
    gap: 8px;
  }
  .person__role svg { width: 14px; height: 18px; }

  .contact {
    position: absolute;
    top: 268px;
    left: 60px; right: 60px;
    display: flex;
    justify-content: center;
    align-items: stretch;
    gap: 22px;
    font-size: 21px;
  }
  .contact__address { text-align: right; display: flex; align-items: center; gap: 12px; line-height: 1.35; }
  .contact__divider { width: 2px; background: var(--brand-blue); }
  .contact__online { display: flex; flex-direction: column; gap: 8px; justify-content: center; }
  .contact__row { display: flex; align-items: center; gap: 10px; }
  .icon { width: 22px; height: 22px; flex: none; }

  .band-rule {
    position: absolute;
    left: 0; right: 0; top: 392px;
    height: 2px;
    background: var(--accent-magenta);
  }
  .band {
    position: absolute;
    left: 0; right: 0; top: 404px; bottom: 0;
    background: linear-gradient(90deg, var(--band-start), var(--band-end));
  }
</style>
</head>
<body>
  <section class="card card--back" aria-label="Card back">
    <div class="wordmark"><span class="wordmark__square"></span>Brask &amp; Partners</div>
    <p class="company-name">Brask and Partners Ltd.</p>
  </section>

  <section class="card card--front" aria-label="Card front">
    <div class="wordmark"><span class="wordmark__square"></span>Brask &amp; Partners</div>

    <div class="person">
      <p class="person__name">Gergely Halmindo</p>
      <p class="person__role">Managing Director |
        <svg viewBox="0 0 14 18" aria-hidden="true"><rect x="1" y="1" width="12" height="16" rx="2" fill="none" stroke="var(--brand-blue)" stroke-width="2"/><rect x="4" y="4" width="6" height="7" fill="var(--brand-blue)"/></svg>
        +36 30 555 0192</p>
    </div>

    <div class="contact">
      <div class="contact__address">
        <p>1047 Budapest<br>Ravaszi str. 17/B, Hungary</p>
        <svg class="icon" viewBox="0 0 22 22" aria-hidden="true"><path d="M11 1a7 7 0 0 0-7 7c0 5 7 13 7 13s7-8 7-13a7 7 0 0 0-7-7z" fill="var(--brand-blue)"/><circle cx="11" cy="8" r="2.6" fill="#fff"/></svg>
      </div>
      <span class="contact__divider"></span>
      <div class="contact__online">
        <p class="contact__row">
          <svg class="icon" viewBox="0 0 22 22" aria-hidden="true"><circle cx="11" cy="11" r="9.5" fill="none" stroke="var(--brand-blue)" stroke-width="2"/><ellipse cx="11" cy="11" rx="4" ry="9.5" fill="none" stroke="var(--brand-blue)" stroke-width="1.6"/><line x1="1.5" y1="11" x2="20.5" y2="11" stroke="var(--brand-blue)" stroke-width="1.6"/></svg>
          www.braskpartnera.hu</p>
        <p class="contact__row">
          <svg class="icon" viewBox="0 0 22 22" aria-hidden="true"><rect x="1" y="4" width="20" height="14" fill="var(--brand-blue)"/><path d="M1 4l10 8 10-8" fill="none" stroke="#fff" stroke-width="1.6"/></svg>
          g.halmindo@braskpartnera.hu</p>
      </div>
    </div>

    <div class="band-rule"></div>
    <div class="band"></div>
  </section>
</body>
</html>
```